Verodex business card

Business card for sustainable investment company called "Verodex". Verodex is an exchange platform selling carbon credits between buyers and sellers. Carbon Credits are an environmental commodity for reducing global carbon emissions.

the card should obviously have our logo and the theme should be sustainability/environment mixed with a trading platform.

Contact Information for Business Card

Logo, Name, Title, Phone, Email

Colors
0054AA
0677BA
7BADD7
CADEEF
E8F1F8
0094D4
00A9DD
6FCCEA
C7EBF8
E9F6FB
00AB8E
00BBA5
67D7C9
C6EFE9
E9F9F6
59FF00
82FF00
B8FF75
E3FFCB
F4FFEA

```html
<!DOCTYPE html>
<html lang="en">
<head>
<meta charset="utf-8">
<title>Verodex business card</title>
<link rel="stylesheet" href="https://fonts.googleapis.com/css2?family=Montserrat:wght@600;700&family=Open+Sans:wght@400;600&display=swap">
<style>
  :root {
    --stage: #eef2f6;
    --navy: #152a50;
    --navy-soft: #1d4266;
    --white: #ffffff;
    --sky: #6fcce a;
    --blue: #4b8fd6;
    --teal: #5cc6e6;
    --accent-a: #4f86d8;
    --accent-b: #62d0e8;
  }
  :root { --sky: #6fccea; }
  * { box-sizing: border-box; margin: 0; padding: 0; }
  html, body { width: 1200px; height: 780px; overflow: hidden; }
  body {
    background: var(--stage);
    display: flex;
    align-items: center;
    justify-content: center;
    gap: 48px;
    font-family: "Open Sans", Arial, sans-serif;
  }
  .card {
    position: relative;
    width: 540px;
    height: 310px;
    border-radius: 22px;
    background: var(--navy);
    overflow: hidden;
    box-shadow: 0 14px 30px rgba(21, 42, 80, 0.25);
  }
  .brand {
    display: flex;
    align-items: center;
    gap: 12px;
    color: var(--white);
    font-family: "Montserrat", Arial, sans-serif;
    font-weight: 700;
    letter-spacing: 1px;
    text-transform: uppercase;
  }
  .brand__dot {
    background: var(--sky);
    border-radius: 4px;
  }

  /* front */
  .card--front .brand {
    position: absolute;
    left: 120px;
    top: 122px;
    font-size: 46px;
  }
  .card--front .brand__dot { width: 38px; height: 38px; }

  /* back */
  .card--back .brand {
    position: absolute;
    left: 32px;
    top: 30px;
    font-size: 30px;
  }
  .card--back .brand__dot { width: 26px; height: 26px; }

  .rule {
    position: absolute;
    left: 250px;
    right: 0;
    top: 138px;
    height: 2px;
    background: var(--white);
  }
  .person {
    position: absolute;
    left: 34px;
    top: 118px;
    padding-left: 18px;
    border-left: 8px solid var(--accent-a);
    border-image: linear-gradient(var(--accent-a), var(--accent-b)) 1;
  }
  .person__name {
    font-family: "Montserrat", Arial, sans-serif;
    font-size: 26px;
    font-weight: 700;
    color: var(--white);
    line-height: 1.1;
  }
  .person__first { color: var(--blue); }
  .person__title {
    font-size: 14px;
    color: var(--white);
    margin-top: 4px;
  }
  .contact {
    position: absolute;
    left: 60px;
    top: 196px;
    list-style: none;
    color: var(--white);
    font-size: 13px;
    line-height: 20px;
  }
  .contact li { display: flex; align-items: center; gap: 10px; }
  .contact svg { width: 13px; height: 13px; fill: var(--blue); }
  .address {
    position: absolute;
    right: 34px;
    top: 160px;
    text-align: right;
    color: var(--white);
    font-size: 13px;
    line-height: 18px;
  }
  .wave {
    position: absolute;
    left: 0;
    bottom: 0;
    width: 540px;
    height: 80px;
  }
</style>
</head>
<body>

  <section class="card card--front" aria-label="Card front">
    <div class="brand"><span class="brand__dot"></span>Verodex</div>
  </section>

  <section class="card card--back" aria-label="Card back">
    <div class="brand"><span class="brand__dot"></span>Verodex</div>
    <div class="rule"></div>

    <div class="person">
      <p class="person__name"><span class="person__first">Mila</span> Hartwell</p>
      <p class="person__title">Managing Director</p>
    </div>

    <ul class="contact">
      <li>
        <svg viewBox="0 0 24 24" aria-hidden="true"><path d="M6.6 10.8a15 15 0 0 0 6.6 6.6l2.2-2.2a1 1 0 0 1 1-.25 11.4 11.4 0 0 0 3.6.57 1 1 0 0 1 1 1V20a1 1 0 0 1-1 1A17 17 0 0 1 3 4a1 1 0 0 1 1-1h3.5a1 1 0 0 1 1 1c0 1.25.2 2.45.57 3.57a1 1 0 0 1-.25 1z"/></svg>
        (555) 014-2290
      </li>
      <li>
        <svg viewBox="0 0 24 24" aria-hidden="true"><path d="M2 5h20v14H2zm2 2v.5l8 5 8-5V7z"/></svg>
        hello@verodex.co
      </li>
      <li>
        <svg viewBox="0 0 24 24" aria-hidden="true"><circle cx="12" cy="12" r="10"/></svg>
        www.verodex.co
      </li>
    </ul>

    <p class="address">1840 Linden Ave. Suite<br>300 Ashford, TX 75210</p>

    <svg class="wave" viewBox="0 0 540 80" preserveAspectRatio="none" aria-hidden="true">
      <defs>
        <linearGradient id="wave-accent" x1="0" x2="1">
          <stop offset="0" stop-color="#4f86d8"/>
          <stop offset="1" stop-color="#62d0e8"/>
        </linearGradient>
      </defs>
      <path d="M0 68 L330 22 Q360 18 380 20 L540 10 L540 0 L380 8 Q350 6 320 12 L0 60 Z" fill="url(#wave-accent)"/>
      <path d="M0 72 L330 26 Q360 22 400 28 L540 18 L540 80 L0 80 Z" fill="#ffffff"/>
    </svg>
  </section>

</body>
</html>
```